Life Coach for Lawyers Business Card Design

Elegant, original, business card design for life coaching service for associate attorneys who work in big law and struggle with stress, overwhelm, and time management. Double sided design.

Target Market(s)

Women associate attorneys who work in big law and struggle with stress, overwhelm, and time management.

Industry/Entity Type

Life Coaching

Contact Information for Business Card

Marissa Pendrell
Life Coach
518.677.3941
calmbriefcounsel.net
marissa@calmbriefcounsel.net
@calmbriefcounsel (Instagram)

Font styles to use
Other font styles liked:
• Silver South font duo. See uploaded files.

Requirements
Must have
• Icons for phone, website, email, and Instagram instead of words. Specific colors used in my logo (171B2B, 421121, FFFFFF)
Nice to have
• Foil. Embossed. Feminine design.
Should not have
• Any colors other than those used in logo. See uploaded files.

```html
<!DOCTYPE html>
<html lang="en">
<head>
<meta charset="utf-8">
<title>Calm Brief Counsel – Business Card</title>
<link rel="stylesheet" href="https://fonts.googleapis.com/css2?family=Cormorant+Garamond:wght@500;600&family=Great+Vibes&family=Montserrat:wght@400&display=swap">
<style>
  :root {
    --ink: #171B2B;
    --wine: #421121;
    --paper: #FFFFFF;
    --silver: #D9D6D8;
    --backdrop: #ECEAEB;
  }
  * { margin: 0; padding: 0; box-sizing: border-box; }
  html, body { width: 1200px; height: 672px; overflow: hidden; background: var(--backdrop); }
  .stage {
    width: 1200px; height: 672px;
    display: flex; align-items: center; justify-content: center; gap: 60px;
  }
  .card {
    width: 500px; height: 286px; position: relative;
    box-shadow: 0 6px 18px rgba(23, 27, 43, 0.18);
  }
  .card-front { background: var(--paper); color: var(--ink); }
  .card-back { background: var(--wine); display: flex; align-items: center; justify-content: center; }

  .person { position: absolute; left: 34px; top: 24px; }
  .person-name {
    font-family: "Great Vibes", cursive;
    font-size: 40px; line-height: 1; color: var(--ink);
  }
  .person-title {
    font-family: "Cormorant Garamond", serif; font-weight: 600;
    font-size: 15px; letter-spacing: 1.5px; color: var(--wine);
    text-transform: uppercase; margin-top: 4px;
  }

  .contact-list {
    position: absolute; left: 34px; bottom: 26px; list-style: none;
    font-family: "Montserrat", sans-serif; font-size: 12.5px; line-height: 1.2; color: var(--ink);
  }
  .contact-list li { display: flex; align-items: center; gap: 9px; margin-top: 7px; }
  .contact-icon { width: 12px; height: 12px; fill: var(--ink); flex: none; }
  .contact-icon-social {
    width: 11px; height: 11px; flex: none; margin: 0 0.5px;
    border: 1.5px solid var(--ink);
  }

  .brand-name {
    position: absolute; right: 30px; bottom: 26px;
    font-family: "Cormorant Garamond", serif; font-weight: 600;
    font-size: 24px; line-height: 1.05; color: var(--wine);
    text-transform: uppercase; letter-spacing: 2px; text-align: right;
  }

  .brand-seal {
    width: 190px; height: 190px; border-radius: 50%;
    border: 1.5px solid var(--silver);
    display: flex; align-items: center; justify-content: center; text-align: center;
  }
  .brand-seal-name {
    font-family: "Cormorant Garamond", serif; font-weight: 600;
    font-size: 19px; line-height: 1.25; letter-spacing: 3px;
    text-transform: uppercase; color: var(--silver);
  }
</style>
</head>
<body>
<main class="stage">
  <section class="card card-front" aria-label="Card front">
    <div class="person">
      <p class="person-name">Marissa Pendrell</p>
      <p class="person-title">Life Coach</p>
    </div>
    <ul class="contact-list">
      <li>
        <svg class="contact-icon" viewBox="0 0 24 24" aria-hidden="true"><path d="M6.6 10.8a15.1 15.1 0 0 0 6.6 6.6l2.2-2.2c.3-.3.7-.4 1-.2 1.1.4 2.3.6 3.6.6.6 0 1 .4 1 1V20c0 .6-.4 1-1 1C10.6 21 3 13.4 3 4c0-.6.4-1 1-1h3.5c.6 0 1 .4 1 1 0 1.3.2 2.5.6 3.6.1.3 0 .7-.2 1z"/></svg>
        <span>518.677.3941</span>
      </li>
      <li>
        <svg class="contact-icon" viewBox="0 0 24 24" aria-hidden="true"><path d="M2 5h20v14H2z M4 7v.5l8 5 8-5V7z" fill-rule="evenodd"/></svg>
        <span>calmbriefcounsel.net</span>
      </li>
      <li>
        <svg class="contact-icon" viewBox="0 0 24 24" aria-hidden="true"><path d="M12 2a10 10 0 1 0 0 20 10 10 0 0 0 0-20zm6.9 9h-3a15 15 0 0 0-1.2-5.6A8 8 0 0 1 18.9 11zM12 4.1c.9 1.3 1.8 3.6 1.9 6.9h-3.8c.1-3.3 1-5.6 1.9-6.9zM9.3 5.4A15 15 0 0 0 8.1 11h-3a8 8 0 0 1 4.2-5.6zM5.1 13h3a15 15 0 0 0 1.2 5.6A8 8 0 0 1 5.1 13zm6.9 6.9c-.9-1.3-1.8-3.6-1.9-6.9h3.8c-.1 3.3-1 5.6-1.9 6.9zm2.7-1.3a15 15 0 0 0 1.2-5.6h3a8 8 0 0 1-4.2 5.6z"/></svg>
        <span>marissa@calmbriefcounsel.net</span>
      </li>
      <li>
        <span class="contact-icon-social" aria-hidden="true"></span>
        <span>@calmbriefcounsel</span>
      </li>
    </ul>
    <p class="brand-name">Calm Brief<br>Counsel</p>
  </section>

  <section class="card card-back" aria-label="Card back">
    <div class="brand-seal">
      <p class="brand-seal-name">Calm<br>Brief<br>Counsel</p>
    </div>
  </section>
</main>
</body>
</html>
```